Flyer-Design für modernes Yogastudio
Zielgruppe
Modernes Yogastudio - Yogastunden ONLINE und STUDIO, sowie Business und Privat Yoga
Zielgruppe: Menschen, die sich etwas Gutes tun wollen, denen ihre Gesundheit wichtig ist. Alle Altersklassen zwischen 20 und 60 Jahren sind willkommen. Yogastunden verschiedener Niveaus.
Aufgabenstellung
A6 Flyer, beidseitig farbig bedruckt.
Modernes Design (siehe www.lumivasa.de)
Am liebsten helle Farben, weiss, grün, klares Design, nicht überladen.
Es soll ein Info Flyer sein, der auf das Yogastudio aufmerksam macht. Die Texte können von der Webseite übernommen werden oder auch geändert werden.

```html
<!DOCTYPE html>
<html lang="de">
<head>
<meta charset="utf-8">
<title>Lumivasa – Flyer</title>
<link rel="stylesheet" href="https://fonts.googleapis.com/css2?family=Amatic+SC:wght@400;700&family=Allura&display=swap">
<style>
  :root {
    --green: #9dc41f;
    --green-soft: #c5dc6a;
    --ornament: #d3e485;
    --ink: #2b2b2b;
    --bg-center: #f9fbec;
    --bg-edge: #edf2bd;
  }
  html, body {
    margin: 0;
    padding: 0;
    overflow: hidden;
  }
  .flyer {
    position: relative;
    width: 851px;
    height: 1200px;
    overflow: hidden;
    background: radial-gradient(ellipse 75% 70% at 50% 62%, var(--bg-center) 0%, #f4f7d8 55%, var(--bg-edge) 100%);
    font-family: "Amatic SC", "Arial Narrow", sans-serif;
    color: var(--green);
  }
  .ornament {
    position: absolute;
    left: 50%;
    width: 154px;
    height: 62px;
    transform: translateX(-50%);
  }
  .ornament--top { top: 130px; }
  .ornament--bottom { top: 721px; }
  .quote {
    position: absolute;
    top: 246px;
    left: 0;
    right: 0;
    margin: 0;
    text-align: center;
    font-weight: 400;
    font-size: 116px;
    line-height: 99px;
    letter-spacing: 1px;
  }
  .brand__dot {
    position: absolute;
    top: 928px;
    left: 50%;
    width: 64px;
    height: 64px;
    margin-left: -32px;
    border-radius: 50%;
    background: var(--green-soft);
  }
  .brand__name {
    position: absolute;
    top: 1020px;
    left: 0;
    right: 0;
    text-align: center;
    font-weight: 700;
    font-size: 62px;
    line-height: 1;
    color: var(--green);
  }
  .brand__location {
    position: absolute;
    top: 1100px;
    left: 0;
    right: 0;
    text-align: center;
    font-family: "Allura", cursive;
    font-size: 58px;
    line-height: 1;
    color: var(--ink);
  }
</style>
</head>
<body>
<main class="flyer">
  <svg class="ornament ornament--top" viewBox="0 0 154 62" role="img" aria-label="Dekoratives Spiral-Ornament">
    <rect x="0" y="0" width="154" height="62" rx="31" fill="var(--ornament)"/>
  </svg>

  <p class="quote">Yoga bringt dich<br>in den Augenblick,<br>der einzige Ort, wo<br>das Leben existiert.</p>

  <svg class="ornament ornament--bottom" viewBox="0 0 154 62" role="img" aria-label="Dekoratives Spiral-Ornament">
    <rect x="0" y="0" width="154" height="62" rx="31" fill="var(--ornament)"/>
  </svg>

  <span class="brand__dot"></span>
  <span class="brand__name">Lumivasa</span>
  <span class="brand__location">Studio Lindenhain</span>
</main>
</body>
</html>
```